Velora Company website for beauty pre & post natal products

i need to have a company website for my new start up company Velora. Velora means woman in latin. My website url is www.velora-mums.example, i have no contents yet. Velora is focus on selling pre and post natal beauty products e.g.: maternity belt, post natal girdles, maternity bra, etc.. products that beautify woman before and after maternity. I would like the website to potray beauty and yet confident woman. i have attached the sample of the product.
Updates

hi creative designers, I'm looking for your creativity that best to portray my company website, a local company based in Singapore that focus on selling beauty pre and post natal products to beautify motherhood and all women out there

Target Market(s)

Women (age 24-40), mother, career woman, etc

Industry/Entity Type

It Company

Number of Pages Required

5+ page

Font styles to use
Serif
Sans Serif

Requirements
Must have
• - Home page
• (highlights of products, company, beauty elegant women with small children, etc)
• - About Us
• Velora is founded in 2015 in Singapore by a proud mommy of 2 sons. During maternity period which before and after pregnancy, it is extremely crucial for woman to give extra care for herself and her body from the effect of pregnancy due to physical and hormonal changes.
• - Products
• - Client's testimonials
• - Contact Us
• - Inquiry Form
Nice to have
• Professional, yet elegant and appealing to women nowadays. It should show level of trust and credibility just from entering the website.
Should not have
• BIG NO to dark colors, gloomy colors or animations.

```html
<!DOCTYPE html>
<html lang="en">
<head>
<meta charset="utf-8">
<title>Velora Company – Pre &amp; Post Natal Beauty</title>
<link href="https://fonts.googleapis.com/css2?family=Cinzel:wght@400;700&family=Ubuntu:wght@300;400;500;700&display=swap" rel="stylesheet">
<style>
:root{
  --red:#d8323a;
  --red-soft:#e9868a;
  --ink:#3c3c3c;
  --grey:#6d6d6d;
  --light:#f3f1ef;
  --white:#ffffff;
  --footer:#4a4543;
  --field:#ffffff;
  --btn-dark:#3e3b3a;
}
*{box-sizing:border-box;margin:0;padding:0}
html,body{width:1200px;height:3308px;overflow:hidden;background:var(--white)}
body{position:relative;font-family:"Ubuntu",sans-serif;color:var(--ink)}
.abs{position:absolute}
.serif{font-family:"Cinzel",serif}

/* header */
.account{top:44px;right:120px;font-size:13px;color:var(--grey);display:flex;gap:22px;align-items:center}
.account .cart{color:var(--red);display:flex;gap:6px;align-items:center}
.brand{top:40px;left:0;width:1200px;text-align:center}
.brand-dot{width:64px;height:64px;border-radius:50%;background:var(--red);margin:0 auto 26px}
.brand-name{font-family:"Cinzel",serif;font-size:48px;color:var(--grey);line-height:50px;letter-spacing:1px}
.brand-tag{font-family:"Cinzel",serif;font-size:28px;color:var(--grey);line-height:32px}
.brand-rule{width:168px;height:3px;background:var(--red-soft);margin:20px auto 0}

.main-nav{top:302px;left:132px;width:938px;display:flex;justify-content:space-between;align-items:center;font-size:16px;color:var(--grey)}
.main-nav .current{color:var(--red);font-weight:500}
.main-nav .sep{width:5px;height:5px;border-radius:50%;background:var(--ink)}

.hero{top:353px;left:0;width:1200px;height:524px;background:linear-gradient(120deg,#e8e1d6 0%,#f6f1ea 35%,#efe5dc 60%,#dcd2c6 100%)}

/* search */
.search{top:877px;left:0;width:1200px;height:80px;background:var(--red);display:flex;align-items:center;padding-left:106px;gap:0}
.search-label{color:var(--white);font-weight:700;font-size:20px;width:216px}
.field{height:36px;background:var(--field);font-size:13px;color:var(--grey);display:flex;align-items:center;padding-left:14px;gap:8px}
.search .btn{height:36px;width:96px;background:var(--btn-dark);color:var(--white);font-size:13px;display:flex;align-items:center;justify-content:center}

/* welcome */
.section-title{left:0;width:1200px;text-align:center;font-family:"Cinzel",serif;font-size:30px;color:var(--ink)}
.section-rule{left:570px;width:60px;height:3px;background:var(--red-soft)}
.welcome-text{top:1112px;left:300px;width:600px;text-align:center;font-size:15px;line-height:21px;color:var(--grey)}
.product-photo{top:1255px;left:386px;width:428px;height:305px;background:linear-gradient(180deg,#efe4d3,#e4d6c1)}
.product-name{top:1652px;left:0;width:1200px;text-align:center;font-family:"Cinzel",serif;font-size:38px}
.product-price{top:1734px;left:0;width:1200px;text-align:center;font-size:24px;font-weight:500}
.product-desc{top:1768px;left:480px;width:240px;text-align:center;font-size:11px;line-height:15px;color:var(--grey)}
.learn{top:1824px;left:513px;width:105px;height:38px;background:#e6e6e6;font-size:13px;color:var(--grey);display:flex;align-items:center;justify-content:center}
.add-cart{top:1824px;left:629px;width:55px;height:38px;background:var(--red);display:flex;align-items:center;justify-content:center}
.see-more{top:1950px;left:0;width:1200px;text-align:center;font-size:22px;letter-spacing:1px;color:var(--ink)}

/* blog */
.blog-bg{top:2091px;left:0;width:1200px;height:613px;background:linear-gradient(100deg,#f6f3f1 0%,#f1ebe6 45%,#e9e0da 75%,#f4efec 100%)}
.post{top:2251px;width:466px}
.post h3{font-weight:400;font-size:18px;line-height:26px;color:var(--ink);height:100px}
.post .date{color:var(--red);font-size:15px;margin-top:4px}
.post p{font-size:14px;line-height:20px;color:var(--grey);margin-top:18px;height:150px}
.post .more{color:var(--red);font-size:15px;margin-top:18px}

.social{top:2682px;left:500px;width:200px;display:flex;justify-content:center;gap:8px}
.social span{width:44px;height:44px;border-radius:50%;background:var(--red);border:3px solid var(--white)}

/* subscribe */
.subscribe{top:2704px;left:0;width:1200px;height:513px;background:var(--red);color:var(--white)}
.sub-title{top:72px;left:0;width:1200px;text-align:center;font-family:"Cinzel",serif;font-size:22px}
.sub-text{top:120px;left:0;width:1200px;text-align:center;font-size:17px}
.sub-input{top:182px;left:246px;width:626px;height:44px;background:var(--white)}
.sub-btn{top:182px;left:872px;width:83px;height:44px;background:var(--btn-dark);font-size:14px;display:flex;align-items:center;justify-content:center}
.stats{top:322px;left:180px;width:840px;display:flex}
.stat{flex:1;text-align:right;padding-right:22px;border-right:2px solid rgba(255,255,255,.7);height:100px;padding-top:20px}
.stat:last-child{border-right:none}
.stat b{display:block;font-family:"Cinzel",serif;font-weight:400;font-size:28px;line-height:30px}
.stat small{display:block;font-size:14px;margin-top:2px}

.site-footer{top:3217px;left:0;width:1200px;height:91px;background:var(--footer);color:var(--white);font-size:15px;display:flex;align-items:center;justify-content:space-between;padding:0 92px}
.site-footer nav{display:flex;gap:28px}
</style>
</head>
<body>

<div class="abs account">
  <span>LOGIN | SIGNUP</span>
  <span class="cart">
    <svg width="16" height="14" viewBox="0 0 16 14"><path d="M0 1h3l2 8h8l2-6H4.5" fill="none" stroke="currentColor" stroke-width="1.6"/><circle cx="6" cy="12" r="1.4" fill="currentColor"/><circle cx="12" cy="12" r="1.4" fill="currentColor"/></svg>
    $ 200,00
  </span>
</div>

<header class="abs brand">
  <div class="brand-dot"></div>
  <div class="brand-name">YOUR LOGO HERE</div>
  <div class="brand-tag">TAG LINE GOES HERE</div>
  <div class="brand-rule"></div>
</header>

<nav class="abs main-nav">
  <span class="current">HOMEPAGE</span><span class="sep"></span>
  <span>PRODUCTS</span><span class="sep"></span>
  <span>SERVICES</span><span class="sep"></span>
  <span>SHIPPING</span><span class="sep"></span>
  <span>PAYMENT</span><span class="sep"></span>
  <span>HELP</span><span class="sep"></span>
  <span>CONTACT</span>
</nav>

<div class="abs hero" role="img" aria-label="Mother resting in bed beside her sleeping baby in soft morning light"></div>

<form class="abs search">
  <span class="search-label">SEARCH PRODUCTS</span>
  <span class="field" style="width:278px;margin-right:10px"></span>
  <span class="field" style="width:176px;margin-right:10px">
    <svg width="10" height="11" viewBox="0 0 10 11"><circle cx="5" cy="3" r="2.6" fill="#6d6d6d"/><path d="M0 11c0-4 10-4 10 0z" fill="#6d6d6d"/></svg>Categories</span>
  <span class="field" style="width:178px;margin-right:16px">
    <svg width="11" height="11" viewBox="0 0 11 11"><path d="M1 10l1-3 6-6 2 2-6 6z" fill="#6d6d6d"/></svg>Details</span>
  <span class="btn">Search</span>
</form>

<h2 class="abs section-title" style="top:1056px">WELCOME TO OUR STORE</h2>
<div class="abs section-rule" style="top:1101px"></div>
<p class="abs welcome-text">FLorem ipsum dolor sit amet voluptatem fugit aut illo omnis explicabo ipsa nemo rem ipsam quasi illo dolores ut voluptatem doloremque perspiciatis beatae magni architeco</p>

<div class="abs product-photo" role="img" aria-label="Cream post natal support belt with pink stripes"></div>
<h2 class="abs product-name">LOREM IPSUM</h2>
<div class="abs product-price">$ 250,00</div>
<p class="abs product-desc">Lorem ipsum dolor sit amet voluptatem fugit aut illo omnis explicabo nemo enim</p>
<span class="abs learn">LEARN MORE</span>
<span class="abs add-cart"><svg width="20" height="17" viewBox="0 0 16 14"><path d="M0 1h3l2 8h8l2-6H4.5z" fill="#fff" stroke="#fff" stroke-width="1.4" stroke-linejoin="round"/><circle cx="6" cy="12" r="1.5" fill="#fff"/><circle cx="12" cy="12" r="1.5" fill="#fff"/></svg></span>
<div class="abs see-more">SEE MORE PRODUCTS</div>

<section class="abs blog-bg" role="img" aria-label="Faded photo of a mother holding her baby"></section>
<h2 class="abs section-title" style="top:2190px">RECENT NEWS FROM BLOG</h2>
<div class="abs section-rule" style="top:2236px"></div>

<article class="abs post" style="left:91px">
  <h3>OMNIS AUT APERIAM AB IPSAM IPSA ODIT AUT APERIAM AUT ASPERNATUR VERITATIS UNDE</h3>
  <div class="date">April 28, 2015</div>
  <p>Lorem ipsum dolor sit amet voluptatem fugit aut illo omnis explicabo nemo enim ipsam quasi illo dolores voluptatem doloremque perspiciatis magni architecto odit, aspernatur magni quae aperiam aut veritatis eos aut voluptas error natus illo inventore aut quasi consequuntur ipsa odit iste sit quae explicabo dicta quasi...</p>
  <div class="more">READ MORE</div>
</article>
<article class="abs post" style="left:651px">
  <h3>IPSAM IPSA ODIT AUT APERIAM AUT ASPERNATUR VERITATIS UNDE OMNIS AUT APERIAM AB</h3>
  <div class="date">April 28, 2015</div>
  <p>Lorem ipsum dolor sit amet voluptatem fugit aut illo omnis explicabo nemo enim ipsam quasi illo dolores voluptatem doloremque perspiciatis magni architecto odit, aspernatur magni quae aperiam aut veritatis eos aut voluptas error natus illo inventore aut quasi consequuntur ipsa odit iste sit quae explicabo dicta quasi...</p>
  <div class="more">READ MORE</div>
</article>

<section class="abs subscribe">
  <h2 class="abs sub-title">PLEASE SUBSCRIBE</h2>
  <p class="abs sub-text">Get our newsletter for various see new release, promo of the month and relationship issues</p>
  <div class="abs sub-input"></div>
  <div class="abs sub-btn">Subscribe</div>
  <div class="abs stats">
    <div class="stat"><b>5 HUNDRED</b><small>Products</small></div>
    <div class="stat"><b>3 HUNDRED</b><small>Customers</small></div>
    <div class="stat"><b>1 HUNDRED</b><small>On Shipping</small></div>
    <div class="stat"><b>8 HUNDRED</b><small>Women use it</small></div>
  </div>
</section>

<div class="abs social" aria-label="Social links">
  <span></span><span></span><span></span><span></span>
</div>

<footer class="abs site-footer">
  <span>© 2015 <b>YOUR COMPANY</b></span>
  <nav><span>About us</span><span>Privacy policy</span><span>Terms and use</span><span>Countries</span><span>FAQ</span><span>Contact</span></nav>
</footer>

</body>
</html>
```